Brightmoor Partners Branding Revamp

We are a consulting company, looking for a way to display and promote our brand. We have 2 sides to the business- Brightmoor (financial) and Partners (cyber security). The financial side products relate to business necessities: card processing, website design/hosting/maintenance, VoIP phone systems. The cyber security side promotes a bundled package of 4 solutions: network vulnerability scan, dark web scan, anti-ransomeware/malware software, and image-level backups. We want people to understand that partnering with Brightmoor Partners gives them “Steady Ground for Business” (tagline). Current badge and logos uploaded.

Target Market(s)

Small businesses

Contact Information for Business Card

Lena Marwick, Vice President, lena@brightmoorpartners.example, 555-806-1937, www.brightmoorpartners.example

Requirements
Nice to have
• I do prefer the darker background for front and back

```html
<!DOCTYPE html>
<html lang="en">
<head>
<meta charset="utf-8">
<title>Brightmoor Partners – Business Card</title>
<link href="https://fonts.googleapis.com/css2?family=Exo+2:wght@500;600&family=Montserrat:wght@400;500;600&display=swap" rel="stylesheet">
<style>
  :root {
    --page-bg: #2a2c30;
    --card-black: #050505;
    --brand-red: #e3141b;
    --deep-red: #a80b10;
    --text-white: #f4f4f4;
    --text-grey: #bdbdbd;
  }
  * { margin: 0; padding: 0; box-sizing: border-box; }
  html, body {
    width: 1200px; height: 781px; overflow: hidden;
    background: var(--page-bg);
  }
  .canvas {
    width: 1200px; height: 781px;
    display: flex; align-items: center; justify-content: center; gap: 48px;
  }
  .card {
    position: relative;
    width: 540px; height: 309px;
    background: var(--card-black);
    overflow: hidden;
    box-shadow: 0 12px 30px rgba(0,0,0,.45);
  }
  .card-swoosh { position: absolute; inset: 0; width: 100%; height: 100%; }

  /* back side */
  .card--back { display: flex; align-items: center; justify-content: center; }
  .back-wordmark {
    display: flex; align-items: center; gap: 12px;
    font-family: "Montserrat", sans-serif; font-weight: 600;
    font-size: 26px; letter-spacing: 6px; color: var(--brand-red);
    text-transform: uppercase;
  }
  .back-wordmark .mark-square { width: 18px; height: 18px; background: var(--brand-red); }

  /* front side */
  .brand-block {
    position: absolute; left: 24px; top: 112px; width: 220px; text-align: center;
    font-family: "Montserrat", sans-serif;
  }
  .brand-name {
    color: var(--text-white); font-weight: 500; font-size: 19px;
    letter-spacing: 6px; text-transform: uppercase;
  }
  .brand-division {
    color: var(--brand-red); font-weight: 600; font-size: 8.5px;
    letter-spacing: 3px; text-transform: uppercase; margin-top: 6px;
  }
  .brand-tagline {
    color: var(--text-grey); font-size: 7px; letter-spacing: 1px;
    text-transform: uppercase; margin-top: 4px;
  }
  .divider {
    position: absolute; left: 258px; top: 92px; width: 1px; height: 130px;
    background: var(--text-grey); transform: rotate(28deg); opacity: .8;
  }
  .contact-block {
    position: absolute; left: 290px; top: 118px;
    font-family: "Montserrat", sans-serif; color: var(--text-white);
  }
  .person-name {
    font-family: "Exo 2", sans-serif; font-weight: 600; font-size: 22px; letter-spacing: .5px;
  }
  .person-title {
    font-family: "Exo 2", sans-serif; color: var(--brand-red);
    font-size: 11px; font-weight: 500; margin-top: 1px; margin-bottom: 10px;
  }
  .contact-list { list-style: none; }
  .contact-list li {
    display: flex; align-items: center; gap: 7px;
    font-size: 9.5px; line-height: 1; margin-bottom: 7px; letter-spacing: .3px;
  }
  .contact-icon { width: 11px; height: 11px; flex: none; }
</style>
</head>
<body>
<main class="canvas">

  <section class="card card--back" aria-label="Card back">
    <div class="back-wordmark"><span class="mark-square"></span>Brightmoor</div>
  </section>

  <section class="card card--front" aria-label="Card front">
    <svg class="card-swoosh" viewBox="0 0 540 309" preserveAspectRatio="none" aria-hidden="true">
      <defs>
        <linearGradient id="redBand" x1="0" y1="0" x2="1" y2="1">
          <stop offset="0" stop-color="#e3141b"/>
          <stop offset="1" stop-color="#a80b10"/>
        </linearGradient>
      </defs>
      <path d="M250 0 H540 V160 C470 70 380 20 250 0 Z" fill="url(#redBand)"/>
      <path d="M300 0 C410 25 490 80 540 150 V175 C480 90 400 30 300 0 Z" fill="#ff2a2f" opacity=".55"/>
      <path d="M170 309 C330 300 450 270 540 220 V309 Z" fill="url(#redBand)"/>
      <path d="M230 309 C360 296 460 264 540 232 V246 C450 280 350 302 230 309 Z" fill="#ff2a2f" opacity=".5"/>
    </svg>

    <div class="brand-block">
      <div class="brand-name">Brightmoor</div>
      <div class="brand-division">Partners</div>
      <div class="brand-tagline">Steady Ground for Business</div>
    </div>

    <div class="divider"></div>

    <div class="contact-block">
      <div class="person-name">Lena Marwick</div>
      <div class="person-title">Vice President</div>
      <ul class="contact-list">
        <li>
          <svg class="contact-icon" viewBox="0 0 12 12" aria-hidden="true"><circle cx="6" cy="6" r="6" fill="#f4f4f4"/><path d="M4 3.2l1 1.3-.6.7c.4.9 1 1.5 1.9 1.9l.7-.6 1.3 1-.6 1C5.8 8.3 3.7 6.2 3.5 4z" fill="#050505"/></svg>
          555-806-1937
        </li>
        <li>
          <svg class="contact-icon" viewBox="0 0 12 12" aria-hidden="true"><circle cx="6" cy="6" r="5.4" fill="none" stroke="#f4f4f4" stroke-width="1.1"/><rect x="3.2" y="4" width="5.6" height="4" fill="none" stroke="#f4f4f4" stroke-width=".8"/><path d="M3.2 4l2.8 2.2L8.8 4" fill="none" stroke="#f4f4f4" stroke-width=".8"/></svg>
          lena@brightmoorpartners.example
        </li>
        <li>
          <svg class="contact-icon" viewBox="0 0 12 12" aria-hidden="true"><circle cx="6" cy="6" r="5.4" fill="none" stroke="#f4f4f4" stroke-width="1.1"/><ellipse cx="6" cy="6" rx="2.2" ry="5" fill="none" stroke="#f4f4f4" stroke-width=".8"/><path d="M1 6h10" stroke="#f4f4f4" stroke-width=".8"/></svg>
          www.brightmoorpartners.example
        </li>
      </ul>
    </div>
  </section>

</main>
</body>
</html>
```